Offshore Energy Projects Management Consultancy needs a business card design

Logo available. We provide teams to deliver engineering consultancy, project management and delivery teams mainly in the offshore renewables sector. The company is all about bringing the right people to a project to deliver the scope.

The business card will be used for all staff.

The business card should be quite simple, vibrant and uncluttered but convey experience, enthusiasm and integration.

Target Market(s)

Energy Project Developers and Tier 1 construction companies

Contact Information for Business Card

Logo should be on the back of the card. I'm happy for the designer to play with the colour of the logo and background colour.

Front of the card should convey all the must have information in a clear and professional manner but without being overly traditional.

Colors

Designer to choose colors to be used in the design.

Requirements
Must have
• Land Line Tel Number, Mobile Tel Number, Email, business address, web address.

```html
<!DOCTYPE html>
<html lang="en">
<head>
<meta charset="utf-8">
<title>Seaward Works Alliance – Business Card</title>
<link rel="stylesheet" href="https://fonts.googleapis.com/css2?family=Open+Sans:wght@400;600;700&display=swap">
<style>
  :root {
    --page-bg: #dcdcdc;
    --card-white: #f7f7f7;
    --card-dark: #1b1b1b;
    --brand-blue: #2a9fdc;
    --edge-blue: #1478c2;
    --rule-blue: #1b6fb8;
    --text-grey: #555555;
    --mark-grey: #6a6a6a;
    --mark-dark: #3a3a3a;
  }
  * { box-sizing: border-box; margin: 0; padding: 0; }
  html, body {
    width: 1200px; height: 856px; overflow: hidden;
    background: var(--page-bg);
    font-family: "Open Sans", sans-serif;
  }
  .canvas {
    width: 1200px; height: 856px;
    display: flex; flex-direction: column;
    align-items: center; justify-content: center; gap: 40px;
  }
  .card {
    width: 620px; height: 354px;
    border-bottom: 4px solid var(--edge-blue);
    border-right: 2px solid var(--edge-blue);
    position: relative;
  }
  .card--front { background: var(--card-white); display: flex; align-items: center; }
  .card--back { background: var(--card-dark); display: flex; align-items: center; justify-content: center; }

  .company-name {
    font-weight: 600; color: var(--mark-grey);
    text-align: center; line-height: 1.15;
    text-transform: uppercase;
  }
  .card--front .company-name { width: 270px; font-size: 24px; letter-spacing: 0.5px; }
  .card--back .company-name { font-size: 40px; color: var(--mark-dark); letter-spacing: 1px; }

  .divider {
    width: 2px; height: 170px; background: var(--rule-blue);
  }
  .details { padding-left: 28px; color: var(--text-grey); }
  .person-name { font-size: 21px; font-weight: 700; color: var(--brand-blue); line-height: 1.1; }
  .person-role { font-size: 16px; margin-bottom: 14px; }
  .address { font-size: 14px; line-height: 1.35; margin-bottom: 14px; }
  .address .building { color: var(--brand-blue); }
  .contact-list { list-style: none; font-size: 14px; line-height: 1.5; }
  .contact-list li { display: flex; align-items: center; gap: 10px; }
  .contact-list svg { width: 14px; height: 14px; flex: none; fill: var(--brand-blue); }
</style>
</head>
<body>
<main class="canvas">
  <section class="card card--front">
    <div style="width:300px;display:flex;justify-content:center;">
      <p class="company-name">Seaward Works Alliance</p>
    </div>
    <span class="divider"></span>
    <div class="details">
      <p class="person-name">Callum Reid</p>
      <p class="person-role">Director</p>
      <p class="address">
        <span class="building">The Harbour House,</span><br>
        120 Quay Road,<br>
        Portmore, PM4 2QX
      </p>
      <ul class="contact-list">
        <li>
          <svg viewBox="0 0 16 16" aria-hidden="true"><path d="M3.5 1 6 1.5 7 5 5.2 6.3a8 8 0 0 0 4.5 4.5L11 9l3.5 1 .5 2.5c0 1-1 2.5-2.5 2.5C6.5 15 1 9.5 1 3.5 1 2 2.5 1 3.5 1z"/></svg>
          +44 1632 960 418
        </li>
        <li>
          <svg viewBox="0 0 16 16" aria-hidden="true"><path d="M4.5 0h7A1.5 1.5 0 0 1 13 1.5v13a1.5 1.5 0 0 1-1.5 1.5h-7A1.5 1.5 0 0 1 3 14.5v-13A1.5 1.5 0 0 1 4.5 0zM4.5 2v10.5h7V2zM8 13.3a.9.9 0 1 0 0 1.8.9.9 0 0 0 0-1.8z"/></svg>
          +44 7700 900 226
        </li>
        <li>
          <svg viewBox="0 0 16 16" aria-hidden="true"><path d="M0 3h16v1L8 9 0 4zM0 5.5l8 5 8-5V13H0z"/></svg>
          hello@seaward.example
        </li>
        <li>
          <svg viewBox="0 0 16 16" aria-hidden="true"><path d="M8 0a8 8 0 1 0 0 16A8 8 0 0 0 8 0zm0 1.5c.9 0 2 1.8 2.3 4.5H5.7C6 3.3 7.1 1.5 8 1.5zM1.6 7h2.9a14 14 0 0 0 0 2H1.6a6.5 6.5 0 0 1 0-2zm4.1 0h4.6a13 13 0 0 1 0 2H5.7a13 13 0 0 1 0-2zm5.8 0h2.9a6.5 6.5 0 0 1 0 2h-2.9a14 14 0 0 0 0-2zM5.7 10h4.6C10 12.7 8.9 14.5 8 14.5S6 12.7 5.7 10z"/></svg>
          www.seaward.example
        </li>
      </ul>
    </div>
  </section>

  <section class="card card--back">
    <p class="company-name">Seaward Works Alliance</p>
  </section>
</main>
</body>
</html>
```